Lantern Business Cards

Need business cards for my employees at my restaurant.

Needs to include:
Our Logo
Lantern Forks & Cellar
Name: Miriam Toddwell
Title : Owner
Address: 847 Pickering Ave. Cedar Bluff City, NM 86519
Web: www.lanternkitchenbay.com
Phone: 505-555-0147
Cell: 505-555-0183
Email: info@lanternkitchenbay.com

```html
<!DOCTYPE html>
<html lang="en">
<head>
<meta charset="utf-8">
<title>Lantern Forks &amp; Cellar – Business Card</title>
<link rel="stylesheet" href="https://fonts.googleapis.com/css2?family=Roboto:wght@400;500;700&display=swap">
<style>
  :root {
    --stage: #666666;
    --paper: #ffffff;
    --ink: #1c1c1c;
    --brand-red: #c0202f;
    --card-black: #1b1b1b;
    --emboss: #2c2c2c;
    --rule: #333333;
  }
  * { box-sizing: border-box; margin: 0; padding: 0; }
  html, body { width: 1200px; height: 900px; overflow: hidden; }
  body {
    background: var(--stage);
    font-family: "Roboto", Arial, sans-serif;
    display: flex;
    flex-direction: column;
    align-items: center;
    justify-content: center;
    gap: 40px;
  }
  .card {
    position: relative;
    width: 700px;
    height: 400px;
    border-radius: 30px;
    overflow: hidden;
  }

  /* Back side */
  .card--back { background: var(--card-black); }
  .back-mark {
    position: absolute;
    inset: 0;
    display: flex;
    align-items: center;
    justify-content: center;
    gap: 28px;
  }
  .back-mark__dot {
    width: 110px; height: 110px;
    border-radius: 50%;
    background: var(--emboss);
  }
  .back-mark__name {
    font-weight: 700;
    font-size: 44px;
    line-height: 1.05;
    color: var(--emboss);
    letter-spacing: 2px;
    text-transform: uppercase;
  }

  /* Front side */
  .card--front { background: var(--paper); }
  .brand {
    position: absolute;
    top: 44px; left: 56px; right: 40px;
    display: flex;
    align-items: center;
    gap: 28px;
  }
  .brand__dot {
    width: 120px; height: 120px;
    border-radius: 50%;
    background: var(--ink);
    flex: none;
  }
  .brand__name {
    font-weight: 700;
    font-size: 44px;
    line-height: 1.05;
    color: var(--brand-red);
    letter-spacing: 2px;
    text-transform: uppercase;
  }
  .person {
    position: absolute;
    left: 56px; top: 222px;
    width: 250px;
    text-align: right;
  }
  .person__name { font-weight: 700; font-size: 30px; color: var(--brand-red); }
  .person__title { font-size: 22px; color: var(--ink); margin-top: 2px; }
  .divider {
    position: absolute;
    left: 330px; top: 196px;
    width: 2px; height: 120px;
    background: var(--rule);
  }
  .contacts {
    position: absolute;
    left: 356px; top: 190px;
    list-style: none;
    font-size: 20px;
    color: var(--ink);
  }
  .contacts li {
    display: flex;
    align-items: center;
    gap: 12px;
    height: 32px;
  }
  .contacts svg { width: 20px; height: 20px; flex: none; fill: var(--brand-red); }
  .address-band {
    position: absolute;
    left: 0; right: 0; bottom: 28px;
    height: 50px;
    background: var(--brand-red);
    color: var(--paper);
    display: flex;
    align-items: center;
    padding-left: 56px;
    gap: 12px;
    font-size: 21px;
    font-weight: 500;
  }
  .address-band svg { width: 20px; height: 24px; fill: var(--paper); }
</style>
</head>
<body>

  <section class="card card--back" aria-label="Card back">
    <div class="back-mark">
      <div class="back-mark__dot"></div>
      <div class="back-mark__name">Lantern<br>Forks &amp; Cellar</div>
    </div>
  </section>

  <section class="card card--front" aria-label="Card front">
    <div class="brand">
      <div class="brand__dot"></div>
      <div class="brand__name">Lantern<br>Forks &amp; Cellar</div>
    </div>

    <div class="person">
      <p class="person__name">Miriam Toddwell</p>
      <p class="person__title">Owner</p>
    </div>

    <div class="divider"></div>

    <ul class="contacts">
      <li>
        <svg viewBox="0 0 24 24"><path d="M6.6 10.8a15.1 15.1 0 0 0 6.6 6.6l2.2-2.2a1 1 0 0 1 1-.25 11.4 11.4 0 0 0 3.6.57 1 1 0 0 1 1 1V20a1 1 0 0 1-1 1A17 17 0 0 1 3 4a1 1 0 0 1 1-1h3.5a1 1 0 0 1 1 1c0 1.25.2 2.45.57 3.57a1 1 0 0 1-.25 1z"/></svg>
        505-555-0147
      </li>
      <li>
        <svg viewBox="0 0 24 24"><path d="M7 1h10a2 2 0 0 1 2 2v18a2 2 0 0 1-2 2H7a2 2 0 0 1-2-2V3a2 2 0 0 1 2-2zm0 3v14h10V4zm5 15.5a1.2 1.2 0 1 0 0 2.4 1.2 1.2 0 0 0 0-2.4z"/></svg>
        505-555-0183
      </li>
      <li>
        <svg viewBox="0 0 24 24"><path d="M2 5h20v14H2zm2 2v.5l8 5 8-5V7zm0 2.9V17h16V9.9l-8 5z"/></svg>
        info@lanternkitchenbay.com
      </li>
      <li>
        <svg viewBox="0 0 24 24"><path d="M12 2a10 10 0 1 0 0 20 10 10 0 0 0 0-20zm-1 17.9A8 8 0 0 1 4.1 11H8a12 12 0 0 0 3 8.9zM8 9H4.3A8 8 0 0 1 11 4.1 12 12 0 0 0 8 9zm5 10.9A12 12 0 0 0 16 11h3.9a8 8 0 0 1-6.9 8.9zM16 9a12 12 0 0 0-3-4.9A8 8 0 0 1 19.7 9zm-2 2a10 10 0 0 1-2 6.5A10 10 0 0 1 10 11zm-4-2a10 10 0 0 1 2-4.5A10 10 0 0 1 14 9z"/></svg>
        www.lanternkitchenbay.com
      </li>
    </ul>

    <div class="address-band">
      <svg viewBox="0 0 20 24"><path d="M10 0a8 8 0 0 0-8 8c0 6 8 16 8 16s8-10 8-16a8 8 0 0 0-8-8zm0 11a3 3 0 1 1 0-6 3 3 0 0 1 0 6z"/></svg>
      847 Pickering Ave. Cedar Bluff City, NM 86519
    </div>
  </section>

</body>
</html>
```